Stabilization Flyer

We are looking for a single document that outlines the info below - we want to emphasize that we can help child cares in the process and then we can help them make any award money go further through our program -
Don’t leave money on the table – as a child care owner you have access to grant money, but time is running out.

President Tallow signed the National Renewal Grant Act of 2021 (NRG). This plan includes $24 billion in child care stabilization grant funding. These funds will help keep early childhood educators and family child care providers keep their doors open and provide a critical step to paving the way for a strong economic recovery and a more equitable future.

Each State has its own application process – most licensed child care centers are eligible for grants with awards up to $400,000 per program. Awarded dollars is based upon your center’s capacity.

Grants are good for the following categories

Child care providers can use stabilization subgrants to cover these expenses:
• Wages and benefits, including increases in compensation for any staff.
• Rent, utilities, facilities maintenance and minor renovations, and insurance.
• Personal protective equipment, cleaning supplies, and other health and safety measures.
• Equipment and supplies used to respond to COVID-19.
• Material goods (i.e., to facilitate play or safe sleep) or services (i.e., food) used for the operation of the program. Yes, Food is an allowable expense.
• Mental health services for children and employees

If you have not applied for the grant, we can help point you in the right direction. Just email stablization@pantrycrateoutlet.com or call 877. 391.6052 and we will send you the links on how to file within your State. No purchase is necessary for this guidance, but we would love the opportunity to show you how we can stretch your purchases by up to 30%.

Target Market(s)

child care centers

Industry/Entity Type

child care is the target

Requirements
Must have
• website www.pantrycrateoutlet.com
Nice to have
• we have a video that could be embedded https://www.pantrycrateoutlet.com/video-resources/

```html
<!DOCTYPE html>
<html lang="en">
<head>
<meta charset="utf-8">
<title>Pantry Crate Outlet – Stabilization Grant Flyer</title>
<link href="https://fonts.googleapis.com/css2?family=Heebo:wght@700;800&family=Roboto:wght@400;500;700&display=swap" rel="stylesheet">
<style>
  :root {
    --blue: #3a8fd3;
    --green: #8ed08a;
    --paper: #f7f7f7;
    --ink: #1f2226;
    --grey: #5d6670;
    --white: #ffffff;
    --photo-a: #c9c1b6;
    --photo-b: #8a95a6;
  }
  * { margin: 0; padding: 0; box-sizing: border-box; }
  html, body { width: 990px; height: 1200px; overflow: hidden; background: var(--paper); }
  .flyer {
    position: relative; width: 990px; height: 1200px; overflow: hidden;
    background: var(--paper); font-family: "Roboto", Arial, sans-serif; color: var(--ink);
  }
  .backdrop { position: absolute; inset: 0; }
  .brand {
    position: absolute; left: 64px; top: 86px; display: flex; align-items: center; gap: 14px;
  }
  .brand-mark { width: 44px; height: 44px; background: var(--blue); }
  .brand-name { font-family: "Roboto", Arial, sans-serif; font-weight: 400; font-size: 42px; color: var(--grey); letter-spacing: -0.5px; }
  .photo { position: absolute; left: 557px; top: 73px; }
  .headline {
    position: absolute; left: 75px; top: 255px; width: 480px;
    border-left: 4px solid var(--white); padding-left: 20px;
    font-family: "Heebo", Arial, sans-serif; font-weight: 800; color: var(--white);
    font-size: 36px; line-height: 44px;
  }
  .intro { position: absolute; left: 70px; width: 850px; font-size: 13.6px; line-height: 18px; text-align: justify; }
  .intro-1 { top: 626px; }
  .intro-2 { top: 698px; }
  .hl { color: var(--blue); font-weight: 500; }
  .category-bar {
    position: absolute; left: 58px; top: 754px; width: 873px; height: 46px;
    background: var(--blue); color: var(--white); border-radius: 3px;
    font-weight: 500; font-size: 28px; line-height: 46px; text-align: center;
  }
  .category-sub {
    position: absolute; left: 0; width: 990px; top: 810px; text-align: center;
    color: var(--blue); font-weight: 500; font-size: 20px;
  }
  .expense-list { position: absolute; top: 848px; list-style: none; width: 400px; }
  .expense-list.left { left: 80px; }
  .expense-list.right { left: 521px; }
  .expense-list li {
    position: relative; padding-left: 22px; font-size: 14.6px; line-height: 18px; margin-bottom: 9px;
  }
  .tick { position: absolute; left: 0; top: 2px; width: 14px; height: 14px; }
  .green-base { position: absolute; left: 0; top: 1072px; width: 990px; height: 128px; background: var(--green); }
  .help-box {
    position: absolute; left: 58px; top: 996px; width: 873px; height: 114px;
    background: #f1f1f1; border: 1px solid #dedede; border-radius: 8px;
    box-shadow: 0 10px 14px -8px rgba(0,0,0,0.45);
    padding: 20px 36px 0; text-align: center; font-size: 14.4px; line-height: 18.5px;
  }
  .contact-row {
    position: absolute; left: 0; top: 1140px; width: 990px;
    display: flex; justify-content: center; align-items: center; gap: 18px;
    font-weight: 700; font-size: 17.5px; color: var(--ink);
  }
  .contact-row .item { display: flex; align-items: center; gap: 6px; }
  .contact-row .sep { font-weight: 400; }
  .contact-row svg { width: 18px; height: 18px; }
</style>
</head>
<body>
<div class="flyer">
  <svg class="backdrop" width="990" height="1200" viewBox="0 0 990 1200" aria-hidden="true">
    <path d="M0,160 Q330,350 690,25 L720,30 Q640,200 580,470 Q320,640 0,532 Z" fill="var(--green)"/>
    <path d="M0,148 Q330,330 678,28 L700,60 Q620,220 570,458 Q310,620 0,518 Z" fill="var(--blue)"/>
  </svg>

  <div class="brand">
    <span class="brand-mark"></span>
    <span class="brand-name">Pantry Crate Outlet</span>
  </div>

  <svg class="photo" width="520" height="520" viewBox="0 0 520 520">
    <defs>
      <linearGradient id="photoTone" x1="0" y1="0" x2="1" y2="1">
        <stop offset="0" stop-color="var(--photo-a)"/>
        <stop offset="1" stop-color="var(--photo-b)"/>
      </linearGradient>
    </defs>
    <circle cx="263" cy="260" r="257" fill="var(--green)"/>
    <circle cx="263" cy="260" r="243" fill="url(#photoTone)" role="img" aria-label="Photo of a smiling family: mother, father and two young children on a sofa"/>
  </svg>

  <h1 class="headline">Don’t leave money on the table –<br>as a child care owner you have access to grant money, but time is running out.</h1>

  <p class="intro intro-1"><span class="hl">President Tallow</span> signed the <span class="hl">National Renewal Grant Act of 2021 (NRG).</span> This plan includes <span class="hl">$24 billion</span> in child care stabilization grant funding. These funds will help keep early childhood educators and family child care providers keep their doors open and provide a critical step to paving the way for a strong economic recovery and a more equitable future.</p>
  <p class="intro intro-2">Each State has its own application process – most licensed child care centers are eligible for grants with awards up to <span class="hl">$400,000 per program.</span> Awarded dollars is based upon your center’s capacity.</p>

  <h2 class="category-bar">Grants are good for the following categories</h2>
  <h3 class="category-sub">Child care providers can use stabilization subgrants to cover these expenses:</h3>

  <ul class="expense-list left">
    <li><svg class="tick" viewBox="0 0 14 14"><circle cx="7" cy="7" r="6.2" fill="none" stroke="var(--blue)" stroke-width="1.2"/><path d="M4 7.2 L6.2 9.2 L10 5" fill="none" stroke="var(--blue)" stroke-width="1.3"/></svg>Wages and benefits, including increases in compensation for any staff.</li>
    <li><svg class="tick" viewBox="0 0 14 14"><circle cx="7" cy="7" r="6.2" fill="none" stroke="var(--blue)" stroke-width="1.2"/><path d="M4 7.2 L6.2 9.2 L10 5" fill="none" stroke="var(--blue)" stroke-width="1.3"/></svg>Rent, utilities, facilities maintenance and minor renovations, and insurance.</li>
    <li><svg class="tick" viewBox="0 0 14 14"><circle cx="7" cy="7" r="6.2" fill="none" stroke="var(--blue)" stroke-width="1.2"/><path d="M4 7.2 L6.2 9.2 L10 5" fill="none" stroke="var(--blue)" stroke-width="1.3"/></svg>Personal protective equipment, cleaning supplies, and other health and safety measures.</li>
  </ul>
  <ul class="expense-list right">
    <li><svg class="tick" viewBox="0 0 14 14"><circle cx="7" cy="7" r="6.2" fill="none" stroke="var(--blue)" stroke-width="1.2"/><path d="M4 7.2 L6.2 9.2 L10 5" fill="none" stroke="var(--blue)" stroke-width="1.3"/></svg>Equipment and supplies used to respond<br>to COVID-19.</li>
    <li><svg class="tick" viewBox="0 0 14 14"><circle cx="7" cy="7" r="6.2" fill="none" stroke="var(--blue)" stroke-width="1.2"/><path d="M4 7.2 L6.2 9.2 L10 5" fill="none" stroke="var(--blue)" stroke-width="1.3"/></svg>Material goods (i.e., to facilitate play or safe sleep) or services (i.e., food) used for the operation of the program. Yes, Food is an allowable expense.</li>
    <li><svg class="tick" viewBox="0 0 14 14"><circle cx="7" cy="7" r="6.2" fill="none" stroke="var(--blue)" stroke-width="1.2"/><path d="M4 7.2 L6.2 9.2 L10 5" fill="none" stroke="var(--blue)" stroke-width="1.3"/></svg>Mental health services for children and employees</li>
  </ul>

  <div class="green-base"></div>

  <p class="help-box">If you have not applied for the grant, we can help point you in the right direction. Just email <span class="hl">stablization@pantrycrateoutlet.com</span> or call <span class="hl">877. 391.6052</span> and we will send you the links on how to file within your State. No purchase is necessary for this guidance, but we would love the opportunity to show you how we can stretch your purchases by up to 30%.</p>

  <div class="contact-row">
    <span class="item"><svg viewBox="0 0 18 18"><circle cx="9" cy="9" r="7.5" fill="none" stroke="var(--ink)" stroke-width="1.3"/><ellipse cx="9" cy="9" rx="3.2" ry="7.5" fill="none" stroke="var(--ink)" stroke-width="1.1"/><path d="M1.5 9 H16.5" stroke="var(--ink)" stroke-width="1.1"/></svg>www.pantrycrateoutlet.com</span>
    <span class="sep">|</span>
    <span class="item"><svg viewBox="0 0 18 18"><circle cx="9" cy="9" r="8" fill="none" stroke="var(--ink)" stroke-width="1.3"/><path d="M6 4.5 L7.8 6.6 L7 8 Q8 10.2 10 11 L11.4 10.2 L13.5 12 Q12.6 13.8 11 13.6 Q5.2 12.4 4.4 7 Q4.4 5.3 6 4.5 Z" fill="none" stroke="var(--ink)" stroke-width="1.1"/></svg>(877) 391-6052</span>
    <span class="sep">|</span>
    <span class="item"><svg viewBox="0 0 18 18"><rect x="1.5" y="4" width="15" height="10" fill="none" stroke="var(--ink)" stroke-width="1.2"/><path d="M1.5 4 L9 10 L16.5 4" fill="none" stroke="var(--ink)" stroke-width="1.2"/></svg>info@pantrycrateoutlet.com</span>
  </div>
</div>
</body>
</html>
```